MS Word Template needed for a company specialized in Insurance and Finance Advising

I am looking for an impressive and memorable Word Template for:

Writing daily letters
Presentations
Agreements
Front Pages for Projects
Finance, pension, tax analyzes ...

Our logo is attached.
We are advising clients in all kind of questions in the finance and insurance industry, we are not selling products, our main business is the advising and to win the trust to all kind of costumers, from young to old from all kind of nations.

```html
<!DOCTYPE html>
<html lang="en">
<head>
<meta charset="utf-8">
<title>Keller Advisory – Stationery Templates</title>
<link rel="stylesheet" href="https://fonts.googleapis.com/css2?family=Montserrat:wght@400;500;600;700;800&display=swap">
<style>
:root{
  --red:#e11f26;
  --red-dark:#9e1016;
  --grey:#8e8e90;
  --grey-light:#c9c9cb;
  --ink:#3a3a3c;
  --bg:#e1e1e2;
  --paper:#ffffff;
}
*{margin:0;padding:0;box-sizing:border-box}
html,body{width:1200px;height:3546px;overflow:hidden}
body{background:var(--bg);font-family:"Montserrat",Arial,sans-serif;color:var(--ink);position:relative}

.page{position:absolute;width:439px;height:565px;background:var(--paper);overflow:hidden}
.stack .page{box-shadow:4px 8px 18px rgba(0,0,0,.18)}

/* wordmark */
.brand{display:flex;align-items:center;gap:5px;color:var(--red);font-weight:700;letter-spacing:.06em;text-transform:uppercase;white-space:nowrap}
.brand .dot{width:9px;height:9px;border-radius:50%;background:var(--red)}

/* photo placeholders */
.photo{position:absolute;background:linear-gradient(120deg,var(--red-dark) 0%,var(--red) 55%,#f0484d 100%)}

/* cover */
.cover .rule{position:absolute;left:0;top:25px;width:268px;height:5px;background:var(--grey-light)}
.cover .web{position:absolute;right:28px;top:20px;font-size:8px;letter-spacing:.2em;color:var(--red)}
.cover .title{position:absolute;left:44px;top:88px;font-weight:800;font-size:46px;line-height:.96}
.title .t1{color:var(--red);display:block}
.title .t2{color:var(--grey);display:block}
.cover .sub{position:absolute;left:46px;top:184px;font-size:11px;letter-spacing:.38em;color:var(--grey)}
.cover .photo{left:0;top:259px;width:439px;height:163px}
.cover .note{position:absolute;left:44px;top:474px;width:182px;font-size:6px;line-height:8px;color:var(--grey)}
.cover .brand{position:absolute;right:50px;top:484px;font-size:11px}

/* letterhead */
.letter .hd-red{position:absolute;top:0;height:78px;background:var(--red)}
.letter .hd-red.a{left:0;width:43px}
.letter .hd-red.b{left:222px;width:178px}
.letter .hd-grey{position:absolute;top:0;left:400px;width:39px;height:78px;background:var(--grey)}
.letter .brand{position:absolute;left:56px;top:32px;font-size:12px}
.letter .contact{position:absolute;right:52px;top:20px;text-align:right;color:#fff;font-size:8px;font-weight:600;line-height:16px}
.letter .icons{position:absolute;left:412px;top:22px;display:flex;flex-direction:column;gap:7px}
.letter h2{position:absolute;left:54px;top:150px;font-size:19px;font-weight:700;color:var(--red)}
.letter .lead{position:absolute;left:54px;top:176px;font-size:6px;color:var(--ink)}
.letter .body{position:absolute;left:54px;top:196px;width:328px;font-size:6px;line-height:8px}
.letter .body p{margin-bottom:9px}
.letter .sig{position:absolute;left:54px;top:455px;width:78px;height:20px;background:linear-gradient(90deg,#d9d9db,#efeff0)}
.letter .signer{position:absolute;left:54px;top:480px;font-size:10px;font-weight:700;color:var(--red)}
.letter .foot{position:absolute;left:0;bottom:0;width:439px;height:28px;background:var(--bg)}
.letter .foot::before{content:"";position:absolute;left:0;top:0;width:439px;height:8px;background:var(--paper)}

/* agreement */
.agree .brand{position:absolute;left:0;right:0;top:34px;justify-content:center;font-size:13px}
.agree .band{position:absolute;left:0;top:76px;width:439px;height:25px;background:var(--red);display:flex;justify-content:center;align-items:center;gap:22px;color:#fff;font-size:8px}
.agree .band span{display:flex;align-items:center;gap:6px}
.agree .doc-title{position:absolute;right:42px;top:126px;font-size:12px;font-weight:600;color:var(--grey)}
.agree .body{position:absolute;left:42px;top:150px;width:356px;font-size:6px;line-height:8px}
.agree h3{font-size:6px;color:var(--red);font-weight:700;margin:0 0 3px}
.agree .body p{margin-bottom:8px}
.agree .fine{font-size:3.6px;line-height:5px;margin-bottom:6px}
.agree .foot{position:absolute;left:0;bottom:0;width:439px;height:22px;background:var(--grey-light)}

/* landscape cover */
.land{position:absolute;left:318px;top:2972px;width:563px;height:438px;background:var(--paper);overflow:hidden}
.land .brand{position:absolute;left:50px;top:40px;font-size:13px}
.land .title{position:absolute;left:46px;top:140px;font-weight:800;font-size:50px;line-height:.96}
.land .note{position:absolute;left:50px;top:276px;width:205px;font-size:6.5px;line-height:8px;color:var(--grey)}
.land .rule{position:absolute;left:0;top:400px;width:294px;height:5px;background:var(--grey-light)}
.land .photo{left:323px;top:0;width:240px;height:438px}
.land .web{position:absolute;left:323px;width:240px;top:402px;text-align:center;font-size:7px;font-weight:700;letter-spacing:.2em;color:#fff}
</style>
</head>
<body>

<!-- stacked set -->
<section class="stack">
  <article class="page agree" style="left:90px;top:250px">
    <div class="brand"><span class="dot"></span>Keller Advisory</div>
    <div class="band">
      <span><svg width="9" height="9" viewBox="0 0 10 10"><path d="M2 1l2 2-1 1.5a6 6 0 0 0 2.5 2.5L7 6l2 2-1.5 1.5C4.5 9 1 5.5.5 2z" fill="#fff"/></svg>123 456 7890</span>
      <span><svg width="9" height="9" viewBox="0 0 10 10"><circle cx="5" cy="5" r="4" fill="none" stroke="#fff"/><path d="M1 5h8M5 1c2 2 2 6 0 8M5 1c-2 2-2 6 0 8" fill="none" stroke="#fff" stroke-width=".7"/></svg>www.yourwebsite.com</span>
      <span><svg width="10" height="8" viewBox="0 0 10 8"><rect x=".5" y=".5" width="9" height="7" fill="none" stroke="#fff"/><path d="M.5.5l4.5 4 4.5-4" fill="none" stroke="#fff"/></svg>info@yourwebsite.com</span>
    </div>
    <div class="doc-title">Company Agreement</div>
    <div class="body">
      <h3>1. Lorem ipsum dolor sit</h3>
      <p>Lorem ipsum dolor sit amet, consectetur adipiscing elit. In maximus ligula at magna auctor, pretium tempor sapien bibendum. Donec quis ultrices elit. Nam posuere risus congue lacinia ultricies. Duis orci risus, rhoncus sed lacus a, iaculis sodales nisi.</p>
      <h3>2. Lorem ipsum dolor sit</h3>
      <p>Vestibulum eu est lacus. Aliquam eu lectus porttitor, rhoncus nisi ut, vestibulum ex. Donec et finibus mauris, nec volutpat sapien. Nullam molestie lacus ut laoreet ornare.</p>
      <h3>3. Lorem ipsum dolor sit</h3>
      <p>Integer et turpis sodales, ornare justo eget, ornare eros. Phasellus in dui sed mauris faucibus varius quis eu tellus. Etiam molestie mauris et fermentum porta.</p>
    </div>
  </article>

  <article class="page letter" style="left:300px;top:170px">
    <div class="hd-red a"></div><div class="hd-red b"></div><div class="hd-grey"></div>
    <div class="brand"><span class="dot"></span>Keller Advisory</div>
    <div class="contact">123 456 7890<br>www.yourwebsite.com<br>info@yourwebsite.com</div>
    <h2>Lorem ipsum</h2>
    <div class="lead">Lorem ipsum dolor sit amet,</div>
    <div class="body">
      <p>Lorem ipsum dolor sit amet, consectetur adipiscing elit. In maximus ligula at magna auctor, pretium tempor sapien bibendum. Donec quis ultrices elit. Nam posuere risus congue lacinia ultricies.</p>
      <p>Vestibulum eu est lacus. Aliquam eu lectus porttitor, rhoncus nisi ut, vestibulum ex. Donec et finibus mauris, nec volutpat sapien. Nullam molestie lacus ut laoreet ornare.</p>
      <p>Integer et turpis sodales, ornare justo eget, ornare eros. Phasellus in dui sed mauris faucibus varius quis eu tellus. Etiam molestie mauris et fermentum porta.</p>
    </div>
    <div class="sig" role="img" aria-label="Handwritten signature"></div>
    <div class="signer">John Doe</div>
  </article>

  <article class="page cover" style="left:560px;top:120px">
    <div class="rule"></div>
    <div class="web">www.yourwebsite.com</div>
    <h1 class="title"><span class="t1">Project</span><span class="t2">Title</span></h1>
    <div class="sub">Lorem ipsum dolor sit amet.</div>
    <div class="photo" role="img" aria-label="Red-toned photo of a business handshake over a signed contract"></div>
    <p class="note">Lorem ipsum dolor sit amet, consectetur adipiscing elit. Donec bibendum bibendum mi, sit amet bibendum urna tempus sed. Phasellus viverra lorem et dignissim vulputate. Fusce feugiat dictum massa.</p>
    <div class="brand"><span class="dot"></span>Keller Advisory</div>
  </article>
</section>

<!-- cover page -->
<article class="page cover" style="left:380px;top:1073px">
  <div class="rule"></div>
  <div class="web">www.yourwebsite.com</div>
  <h1 class="title"><span class="t1">Project</span><span class="t2">Title</span></h1>
  <div class="sub">Lorem ipsum dolor sit amet.</div>
  <div class="photo" role="img" aria-label="Red-toned photo of a business handshake over a signed contract"></div>
  <p class="note">Lorem ipsum dolor sit amet, consectetur adipiscing elit. Donec bibendum bibendum mi, sit amet bibendum urna tempus sed. Phasellus viverra lorem et dignissim vulputate. Fusce feugiat dictum massa.</p>
  <div class="brand"><span class="dot"></span>Keller Advisory</div>
</article>

<!-- letterhead -->
<article class="page letter" style="left:380px;top:1706px">
  <div class="hd-red a"></div><div class="hd-red b"></div><div class="hd-grey"></div>
  <div class="brand"><span class="dot"></span>Keller Advisory</div>
  <div class="contact">123 456 7890<br>www.yourwebsite.com<br>info@yourwebsite.com</div>
  <div class="icons">
    <svg width="10" height="10" viewBox="0 0 10 10"><path d="M2 1l2 2-1 1.5a6 6 0 0 0 2.5 2.5L7 6l2 2-1.5 1.5C4.5 9 1 5.5.5 2z" fill="none" stroke="#fff" stroke-width=".8"/></svg>
    <svg width="10" height="10" viewBox="0 0 10 10"><circle cx="5" cy="5" r="4" fill="none" stroke="#fff" stroke-width=".8"/><path d="M1 5h8M5 1c2 2 2 6 0 8M5 1c-2 2-2 6 0 8" fill="none" stroke="#fff" stroke-width=".6"/></svg>
    <svg width="10" height="8" viewBox="0 0 10 8"><rect x=".5" y=".5" width="9" height="7" fill="none" stroke="#fff" stroke-width=".8"/><path d="M.5.5l4.5 4 4.5-4" fill="none" stroke="#fff" stroke-width=".8"/></svg>
  </div>
  <h2>Lorem ipsum</h2>
  <div class="lead">Lorem ipsum dolor sit amet,</div>
  <div class="body">
    <p>Lorem ipsum dolor sit amet, consectetur adipiscing elit. In maximus ligula at magna auctor, pretium tempor sapien bibendum. Donec quis ultrices elit. Nam posuere risus congue lacinia ultricies. Duis orci risus, rhoncus sed lacus a, iaculis sodales nisi. Sed sit amet eros erat. Vivamus a urna in est tincidunt consequat. Duis erat felis, pharetra sed nisi in, vehicula ornare arcu. Maecenas ut sagittis lorem.</p>
    <p>Vestibulum eu est lacus. Aliquam eu lectus porttitor, rhoncus nisi ut, vestibulum ex. Donec et finibus mauris, nec volutpat sapien. Nullam molestie lacus ut laoreet ornare. Pellentesque massa elit, volutpat sed lorem quis, tincidunt vehicula velit. Duis fringilla interdum leo, ut dapibus augue sodales vel. Donec felis urna, vulputate sit amet malesuada posuere.</p>
    <p>Integer et turpis sodales, ornare justo eget, ornare eros. Phasellus in dui sed mauris faucibus varius quis eu tellus. Etiam molestie mauris et fermentum porta. Donec mattis cursus sollicitudin. Donec ut tempor nibh, eget volutpat ante. Nunc id ante velit. Vestibulum vitae elit vitae lorem tristique ornare a sed purus. Curabitur ultricies ipsum mauris, ac porttitor ipsum sollicitudin non.</p>
  </div>
  <div class="sig" role="img" aria-label="Handwritten signature"></div>
  <div class="signer">John Doe</div>
  <div class="foot"></div>
</article>

<!-- agreement -->
<article class="page agree" style="left:380px;top:2339px">
  <div class="brand"><span class="dot"></span>Keller Advisory</div>
  <div class="band">
    <span><svg width="9" height="9" viewBox="0 0 10 10"><path d="M2 1l2 2-1 1.5a6 6 0 0 0 2.5 2.5L7 6l2 2-1.5 1.5C4.5 9 1 5.5.5 2z" fill="#fff"/></svg>123 456 7890</span>
    <span><svg width="9" height="9" viewBox="0 0 10 10"><circle cx="5" cy="5" r="4" fill="none" stroke="#fff"/><path d="M1 5h8M5 1c2 2 2 6 0 8M5 1c-2 2-2 6 0 8" fill="none" stroke="#fff" stroke-width=".7"/></svg>www.yourwebsite.com</span>
    <span><svg width="10" height="8" viewBox="0 0 10 8"><rect x=".5" y=".5" width="9" height="7" fill="none" stroke="#fff"/><path d="M.5.5l4.5 4 4.5-4" fill="none" stroke="#fff"/></svg>info@yourwebsite.com</span>
  </div>
  <div class="doc-title">Company Agreement</div>
  <div class="body">
    <h3>1. Lorem ipsum dolor sit</h3>
    <p>Lorem ipsum dolor sit amet, consectetur adipiscing elit. In maximus ligula at magna auctor, pretium tempor sapien bibendum. Donec quis ultrices elit. Nam posuere risus congue lacinia ultricies. Duis orci risus, rhoncus sed lacus a, iaculis sodales nisi. Sed sit amet eros erat. Vivamus a urna in est tincidunt consequat. Duis erat felis, pharetra sed nisi in, vehicula ornare arcu. Maecenas ut sagittis lorem. Nunc ullamcorper diam at mattis pretium.</p>
    <h3>2. Lorem ipsum dolor sit</h3>
    <p>Vestibulum eu est lacus. Aliquam eu lectus porttitor, rhoncus nisi ut, vestibulum ex. Donec et finibus mauris, nec volutpat sapien. Nullam molestie lacus ut laoreet ornare. Pellentesque massa elit, volutpat sed lorem quis, tincidunt vehicula velit. Duis fringilla interdum leo, ut dapibus augue sodales vel. Morbi luctus lacinia quam, vel dapibus odio vestibulum vitae.</p>
    <h3>3. Lorem ipsum dolor sit</h3>
    <p>Integer et turpis sodales, ornare justo eget, ornare eros. Phasellus in dui sed mauris faucibus varius quis eu tellus. Etiam molestie mauris et fermentum porta. Donec mattis cursus sollicitudin. Donec ut tempor nibh, eget volutpat ante. Nunc id ante velit. Vestibulum vitae elit vitae lorem tristique ornare a sed purus. Curabitur ultricies ipsum mauris, ac porttitor ipsum sollicitudin non.</p>
    <p class="fine">Lorem ipsum dolor sit amet, consectetur adipiscing elit. In maximus ligula at magna auctor, pretium tempor sapien bibendum. Donec quis ultrices elit. Nam posuere risus congue lacinia ultricies. Duis orci risus, rhoncus sed lacus a, iaculis sodales nisi. Sed sit amet eros erat. Vivamus a urna in est tincidunt consequat. Duis erat felis, pharetra sed nisi in, vehicula ornare arcu. Maecenas ut sagittis lorem. Nunc ullamcorper diam at mattis pretium. Vestibulum lacinia feugiat neque, nec laoreet leo.</p>
    <p class="fine">Vestibulum eu est lacus. Aliquam eu lectus porttitor, rhoncus nisi ut, vestibulum ex. Donec et finibus mauris, nec volutpat sapien. Nullam molestie lacus ut laoreet ornare. Pellentesque massa elit, volutpat sed lorem quis, tincidunt vehicula velit. Duis fringilla interdum leo, ut dapibus augue sodales vel. Morbi luctus lacinia quam, vel dapibus odio vestibulum vitae. Donec felis urna, vulputate sit amet malesuada posuere, vestibulum in leo. Curabitur nulla dolor, consequat id semper pretium, sagittis eget mauris. Phasellus lobortis neque congue urna efficitur efficitur. Maecenas in facilisis diam. Integer et turpis sodales, ornare justo eget, ornare eros. Phasellus in dui sed mauris faucibus varius quis eu tellus. Etiam molestie mauris et fermentum porta. Donec mattis cursus sollicitudin. Donec ut tempor nibh, eget volutpat ante. Nunc id ante velit.</p>
  </div>
  <div class="foot"></div>
</article>

<!-- landscape cover -->
<article class="land">
  <div class="brand"><span class="dot"></span>Keller Advisory</div>
  <h1 class="title"><span class="t1">Project</span><span class="t2">Title</span></h1>
  <p class="note">Lorem ipsum dolor sit amet, consectetur adipiscing elit. Donec bibendum bibendum mi, sit amet bibendum urna tempus sed. Phasellus viverra lorem et dignissim vulputate. Fusce feugiat dictum massa. Lorem ipsum dolor sit amet, consectetur adipiscing elit. Donec bibendum bibendum mi, sit amet bibendum urna tempus sed. Phasellus viverra lorem et dignissim vulputate. Fusce feugiat dictum massa.</p>
  <div class="rule"></div>
  <div class="photo" role="img" aria-label="Red-toned photo of hands working on a laptop and documents"></div>
  <div class="web">www.yourwebsite.com</div>
</article>

</body>
</html>
```